Creative Photography Business Card

Looking for a unique, creative, elegant, sophisticated and professional business card for my photography business.

I specialise in children, families, modelling, weddings and special event photography

Things to include:
Logo - will attach
Email: hello@mirabellwoodsphoto.com.au
web:www.mirabellwoodsphoto.com.au
Ph: 0438 502 671

I will also upload some of my work that you may like to use.

Please be creative and unique in your designs.

```html
<!DOCTYPE html>
<html lang="en">
<head>
<meta charset="utf-8">
<title>Mirabell Woods Photography – Business Card</title>
<link rel="stylesheet" href="https://fonts.googleapis.com/css2?family=Damion&family=Quicksand:wght@500&display=swap">
<style>
  :root {
    --page: #ffffff;
    --wall-dark: #1f1f1f;
    --wall-mid: #2e2e2e;
    --wall-light: #3a3a3a;
    --print-pink: #e23ad8;
    --print-violet: #6a2fe0;
    --ink: #ffffff;
  }
  * { margin: 0; padding: 0; box-sizing: border-box; }
  html, body {
    width: 1200px;
    height: 702px;
    overflow: hidden;
    background: var(--page);
  }
  .card {
    position: absolute;
    left: 59px;
    top: 56px;
    width: 1082px;
    height: 588px;
    overflow: hidden;
  }
  .card__wall {
    position: absolute;
    inset: 0;
    background: linear-gradient(180deg, var(--wall-mid) 0%, var(--wall-dark) 55%, var(--wall-light) 100%);
  }
  .card__print-band {
    position: absolute;
    left: 0;
    top: 0;
    width: 208px;
    height: 100%;
    background:
      linear-gradient(90deg, rgba(0,0,0,0) 80%, rgba(40,20,60,0.6) 100%),
      linear-gradient(180deg, var(--print-pink) 0%, var(--print-violet) 35%, var(--print-pink) 65%, var(--print-violet) 100%);
  }
  .card__content {
    position: absolute;
    left: 208px;
    right: 0;
    top: 0;
    bottom: 0;
    color: var(--ink);
    font-family: "Quicksand", sans-serif;
    font-weight: 500;
  }
  .card__line {
    position: absolute;
    left: 0;
    right: 0;
    text-align: center;
    white-space: nowrap;
    line-height: 1.2;
  }
  .card__tagline {
    top: 154px;
    font-size: 20px;
    letter-spacing: 0.8px;
  }
  .card__name {
    top: 186px;
    font-family: "Damion", cursive;
    font-weight: 400;
    font-size: 64px;
    line-height: 1;
  }
  .card__email {
    top: 286px;
    font-size: 26px;
    letter-spacing: 0.8px;
  }
  .card__website {
    top: 331px;
    font-size: 32px;
    letter-spacing: 1px;
  }
  .card__phone {
    top: 380px;
    font-size: 29px;
    letter-spacing: 1px;
  }
</style>
</head>
<body>
  <div class="card">
    <div class="card__wall" role="img" aria-label="Dark painted brick wall texture"></div>
    <div class="card__print-band" role="img" aria-label="Pink and violet leopard print pattern band"></div>
    <div class="card__content">
      <p class="card__line card__tagline">Spealization in children, families, modelling, weddings, &amp; special events</p>
      <h1 class="card__line card__name">Mirabell Woods Photography</h1>
      <p class="card__line card__email">Email: hello@mirabellwoodsphoto.com.au</p>
      <p class="card__line card__website">Website: Mirabellwoodsphoto.com.au</p>
      <p class="card__line card__phone">Phone: 0438 502 671</p>
    </div>
  </div>
</body>
</html>
```